US Recruiting Firm Needs Dynamic Tri-Fold Brochure

Need tri-fold professional brochure for HR recruiting and consulting firm based in the US.

Target Market(s)

Clients seeking administrative and human resources talent

Industry/Entity Type

Recruitment

Font styles to use
Sans Serif

Requirements
Should not have
• No weird shapes
• No heavy geometric shapes -- I prefer curvy lines
• Not a dark brochure

```html
<!DOCTYPE html>
<html lang="en">
<head>
<meta charset="utf-8">
<title>Piedmont Office Talent – Tri-Fold Brochure</title>
<link rel="stylesheet" href="https://fonts.googleapis.com/css2?family=Montserrat:wght@400;600;700&family=Didact+Gothic&display=swap">
<style>
  :root{
    --bg:#e6e7e9;
    --paper:#ffffff;
    --navy:#173a57;
    --navy-deep:#0f2c44;
    --orange:#d9560f;
    --orange-text:#f07a1a;
    --lime:#9cc42a;
    --ink:#3a3f45;
    --photo-office:#c9d3dc;
    --photo-office-2:#8fa0ae;
    --photo-team:#b59a84;
    --photo-team-2:#e2d6cc;
    --photo-portrait:#a6a2a0;
    --photo-portrait-2:#d8d4d0;
  }
  *{box-sizing:border-box;margin:0;padding:0}
  html,body{width:1200px;height:800px;overflow:hidden;background:var(--bg)}
  .brochure{position:absolute;left:120px;top:40px;width:960px;height:720px;display:flex;box-shadow:0 10px 30px rgba(0,0,0,.18)}
  .panel{position:relative;width:320px;height:720px;background:var(--paper);overflow:hidden}
  .panel + .panel{border-left:1px solid #e3e5e8}
  .panel svg.layer{position:absolute;left:0;top:0;width:320px;height:720px}

  /* About panel */
  .about-title{position:absolute;left:36px;top:58px;width:250px;height:50px;
    font:700 22px/50px "Montserrat",sans-serif;color:#fff;text-align:center;letter-spacing:.5px}
  .about-copy{position:absolute;left:36px;top:136px;width:252px;
    font:400 12px/1.5 "Didact Gothic",sans-serif;color:var(--ink)}
  .about-copy p + p{margin-top:16px}

  /* Contact panel */
  .cta{position:absolute;left:26px;top:418px;width:280px;color:#fff;font-family:"Montserrat",sans-serif}
  .cta-lead{font:700 21px/1.15 "Montserrat",sans-serif;letter-spacing:.5px}
  .cta-small{font:400 12px/1.3 "Didact Gothic",sans-serif;letter-spacing:.8px;text-transform:uppercase}
  .cta-strong{font:700 14px/1.25 "Montserrat",sans-serif;letter-spacing:.8px}
  .cta-phone{font:700 17px/1.4 "Montserrat",sans-serif;letter-spacing:1px;margin-top:10px}
  .cta-mail{font:400 12.5px/1.3 "Didact Gothic",sans-serif;margin-top:6px}
  .web{position:absolute;left:0;width:100%;top:640px;text-align:center;
    font:600 17px/1 "Montserrat",sans-serif;color:var(--navy);letter-spacing:.5px}

  /* Cover panel */
  .brand{position:absolute;left:30px;top:32px;display:flex;align-items:center;gap:10px}
  .brand-dot{width:26px;height:26px;border-radius:50%;background:var(--navy)}
  .brand-name{font:700 16px/1.1 "Montserrat",sans-serif;color:var(--navy);letter-spacing:.5px}
  .brand-tag{font:600 8.5px/1.3 "Montserrat",sans-serif;color:var(--navy);margin-top:3px}
  .cover-line{position:absolute;left:40px;top:576px;width:260px;
    font:600 20px/1.2 "Montserrat",sans-serif;color:var(--orange-text);letter-spacing:.8px;text-transform:uppercase}
</style>
</head>
<body>
<main class="brochure">

  <!-- Inside flap: About -->
  <section class="panel panel-about">
    <svg class="layer" viewBox="0 0 320 720" aria-hidden="true">
      <path d="M36 64 Q160 50 286 58 L286 100 Q160 112 36 110 Z" fill="var(--navy)"/>
    </svg>
    <h2 class="about-title">ABOUT US</h2>
    <div class="about-copy">
      <p>Piedmont Office Talent is a recruiting and search firm that specializes in providing top-notch administrative and human resources talent. We provide best-in-class talent to companies seeking to attract and retain the best employees, simplify their recruiting process, increase efficiency, and optimize productivity.</p>
      <p>Each search is customized based on the client's requirements. We provide quality, timely, and efficient services. Our recruiters are highly skilled in identifying, screening, interviewing, and assessing candidates across various industries. We develop a partnership with our client and candidate in order to make the recruitment process a success for both parties.</p>
    </div>
    <svg class="layer" viewBox="0 0 320 720">
      <defs>
        <linearGradient id="teamGrad" x1="0" y1="0" x2="1" y2="1">
          <stop offset="0" stop-color="var(--photo-team-2)"/>
          <stop offset="1" stop-color="var(--photo-team)"/>
        </linearGradient>
      </defs>
      <path role="img" aria-label="Photo: smiling team collaborating around a laptop at a meeting table" d="M0 585 Q170 545 320 522 L320 700 Q160 712 0 716 Z" fill="url(#teamGrad)"/>
      <path d="M0 716 Q160 712 320 700 L320 704 Q160 716 0 720 Z" fill="var(--lime)"/>
    </svg>
  </section>

  <!-- Back panel: Contact -->
  <section class="panel panel-contact">
    <svg class="layer" viewBox="0 0 320 720">
      <defs>
        <linearGradient id="officeGrad" x1="0" y1="0" x2="0" y2="1">
          <stop offset="0" stop-color="#eef2f5"/>
          <stop offset="0.6" stop-color="var(--photo-office)"/>
          <stop offset="1" stop-color="var(--photo-office-2)"/>
        </linearGradient>
      </defs>
      <rect role="img" aria-label="Photo: business people talking in a bright glass-walled office" x="0" y="0" width="320" height="440" fill="url(#officeGrad)"/>
      <path d="M0 420 Q170 400 320 360 L320 560 Q170 590 0 610 Z" fill="var(--orange)"/>
      <path d="M0 716 Q160 712 320 700 L320 704 Q160 716 0 720 Z" fill="var(--lime)"/>
    </svg>
    <div class="cta">
      <p class="cta-lead">TO LEARN MORE</p>
      <p class="cta-small">and request a</p>
      <p class="cta-strong">FREE CONSULTATION</p>
      <p class="cta-small">contact us today</p>
      <p class="cta-phone">CALL – 555 014 2288</p>
      <p class="cta-mail">info@piedmonttalent.com</p>
    </div>
    <p class="web">www.piedmonttalent.com</p>
  </section>

  <!-- Front cover -->
  <section class="panel panel-cover">
    <svg class="layer" viewBox="0 0 320 720">
      <defs>
        <linearGradient id="portraitGrad" x1="0" y1="0" x2="1" y2="1">
          <stop offset="0" stop-color="var(--photo-portrait-2)"/>
          <stop offset="1" stop-color="var(--photo-portrait)"/>
        </linearGradient>
      </defs>
      <rect x="0" y="0" width="320" height="720" fill="#f1f1f1"/>
      <rect role="img" aria-label="Photo: confident professional woman in glasses with colleagues behind her" x="0" y="110" width="320" height="440" fill="url(#portraitGrad)"/>
      <path d="M0 520 Q150 500 320 460 L320 700 Q160 712 0 716 Z" fill="var(--navy-deep)"/>
      <path d="M0 716 Q160 712 320 700 L320 704 Q160 716 0 720 Z" fill="var(--lime)"/>
    </svg>
    <div class="brand">
      <span class="brand-dot"></span>
      <div>
        <p class="brand-name">PIEDMONT OFFICE TALENT</p>
        <p class="brand-tag">Human Resources Staffing &amp; Consulting</p>
      </div>
    </div>
    <h1 class="cover-line">Specializing in<br>administrative<br>&amp; HR talent</h1>
  </section>

</main>
</body>
</html>
```